Merchandising Kaffeebohnen mit Firmen Branding
Zielgruppe
Willkommen bei KLV Talmetall, Ihrem internationalen Experten für smarte Recycling- und Verwertungslösungen in der Elektronikbranche. Wir steigern die nachhaltige und wirtschaftliche Performance Ihres Unternehmens mit maßgeschneiderten und CO2-reduzierenden Recyclinglösungen für Lötzinn und edelmetallhaltige Produktionsabfälle. Mit unserer proaktiven Beratung helfen wir Ihrem Unternehmen, nicht nur umweltfreundlich zu agieren, sondern leisten einen messbaren Beitrag für eine zukunftsorientierte Marktpositionierung!
Aufgabenstellung
Modern & schlicht
Wir haben eine Espresso Event und dazu unseren eigenen Kaffee und dafür benötigen wir ein Design.

```html
<!DOCTYPE html>
<html lang="de">
<head>
<meta charset="utf-8">
<title>Espresso Ganze Bohne – KLV Talmetall</title>
<link rel="stylesheet" href="https://fonts.googleapis.com/css2?family=Montserrat:wght@300;400;600;700&family=Oswald:wght@300;500;700&display=swap">
<style>
  :root {
    --backdrop: #5e5e5e;
    --bag-black: #151515;
    --gold: #b39a62;
    --gold-light: #cdb784;
    --gold-dark: #8f7845;
    --white: #f4f4f4;
    --ink: #1c1a16;
    --bean-mid: #6b3b20;
    --bean-dark: #3a1f12;
  }
  * { box-sizing: border-box; margin: 0; padding: 0; }
  html, body { width: 1200px; height: 1200px; overflow: hidden; }
  body {
    background: var(--backdrop);
    font-family: "Montserrat", sans-serif;
    position: relative;
  }

  /* front panel */
  .front-panel {
    position: absolute;
    left: 230px; top: 80px;
    width: 600px; height: 1040px;
    background: var(--bag-black);
  }
  .brand-name {
    position: absolute;
    top: 170px; left: 0; width: 100%;
    text-align: center;
    font-weight: 600;
    font-size: 40px;
    letter-spacing: 1px;
    color: var(--white);
  }
  .product-title {
    position: absolute;
    top: 300px; left: 0; width: 100%;
    text-align: center;
    font-weight: 700;
    font-size: 98px;
    letter-spacing: 1px;
    color: var(--gold);
    line-height: 1;
  }
  .product-subtitle {
    position: absolute;
    top: 412px; left: 0; width: 100%;
    text-align: center;
    font-weight: 300;
    font-size: 52px;
    color: var(--gold);
    line-height: 1;
  }
  .strength-scale {
    position: absolute;
    top: 480px; left: 50%;
    transform: translateX(-50%);
    width: 150px; height: 36px;
  }
  .pattern-area {
    position: absolute;
    top: 530px; left: 30px;
    width: 540px; height: 400px;
    background:
      radial-gradient(circle at 52% 52%, var(--bean-mid) 0%, var(--bean-dark) 22%, rgba(179,154,98,0.35) 34%, rgba(21,21,21,0) 62%),
      linear-gradient(135deg, #2a2a2a 0%, var(--bag-black) 60%, #2b2518 100%);
  }
  .net-weight {
    position: absolute;
    top: 950px; left: 0; width: 100%;
    text-align: center;
    font-weight: 300;
    font-size: 42px;
    line-height: 1;
    color: var(--gold);
  }

  /* side gusset */
  .side-panel {
    position: absolute;
    left: 840px; top: 80px;
    width: 200px; height: 1040px;
    background: linear-gradient(180deg, var(--gold-dark) 0%, var(--gold) 35%, var(--gold-light) 100%);
    color: var(--ink);
    font-family: "Oswald", sans-serif;
  }
  .side-brand {
    position: absolute;
    top: 470px; left: 0; width: 100%;
    text-align: center;
    font-family: "Montserrat", sans-serif;
    font-weight: 600;
    font-size: 17px;
    color: var(--white);
  }
  .side-title {
    position: absolute;
    top: 600px; left: 0; width: 100%;
    text-align: center;
    font-weight: 700;
    font-size: 38px;
    line-height: 1;
  }
  .side-subtitle {
    position: absolute;
    top: 646px; left: 0; width: 100%;
    text-align: center;
    font-weight: 300;
    font-size: 22px;
    line-height: 1;
  }
  .side-strength {
    position: absolute;
    top: 680px; left: 50%;
    transform: translateX(-50%);
    width: 60px; height: 16px;
  }
  .side-copy {
    position: absolute;
    top: 715px; left: 22px; width: 156px;
    font-weight: 300;
    font-size: 12.5px;
    line-height: 1.55;
    text-align: justify;
  }
</style>
</head>
<body>

<section class="front-panel">
  <div class="brand-name">KLV Talmetall</div>
  <h1 class="product-title">ESPRESSO</h1>
  <p class="product-subtitle">GANZE BOHNE</p>

  <svg class="strength-scale" viewBox="0 0 150 36" aria-label="Stärke 4 von 6">
    <g fill="var(--gold)">
      <ellipse cx="12" cy="18" rx="8.5" ry="16"/>
      <ellipse cx="37" cy="18" rx="8.5" ry="16"/>
      <ellipse cx="62" cy="18" rx="8.5" ry="16"/>
      <ellipse cx="87" cy="18" rx="8.5" ry="16"/>
    </g>
    <g fill="var(--white)">
      <ellipse cx="112" cy="18" rx="8.5" ry="16"/>
      <ellipse cx="137" cy="18" rx="8.5" ry="16"/>
    </g>
  </svg>

  <div class="pattern-area" role="img" aria-label="Dekoratives Muster aus weißen und goldenen Sechsecken mit mittigem Foto gerösteter Kaffeebohnen"></div>

  <div class="net-weight">250 g</div>
</section>

<aside class="side-panel">
  <div class="side-brand">KLV Talmetall</div>
  <h2 class="side-title">ESPRESSO</h2>
  <p class="side-subtitle">GANZE BOHNE</p>
  <svg class="side-strength" viewBox="0 0 60 16" aria-label="Stärke 4 von 6">
    <g fill="var(--ink)">
      <ellipse cx="5" cy="8" rx="3.6" ry="7"/>
      <ellipse cx="15" cy="8" rx="3.6" ry="7"/>
      <ellipse cx="25" cy="8" rx="3.6" ry="7"/>
      <ellipse cx="35" cy="8" rx="3.6" ry="7"/>
    </g>
    <g fill="var(--white)">
      <ellipse cx="45" cy="8" rx="3.6" ry="7"/>
      <ellipse cx="55" cy="8" rx="3.6" ry="7"/>
    </g>
  </svg>
  <p class="side-copy">Lorem ipsum dolor sit amet, consectetuer adipiscing elit, sed diam nonummy nibh euismod tincidunt ut laoreet dolore magna aliquam erat volutpat. Ut wisi enim ad minim veniam, quis nostrud exerci tation ullamcorper suscipit lobortis nisl ut aliquip ex ea commodo consequat. Duis autem vel eum iriure dolor in hendrerit in.</p>
</aside>

</body>
</html>
```